2nd Generation Blind Manufacturer & Retailer Needs A Stationary Set

We need a stationary set for a family business located the in the Whitsundays (QLD). We retail and manufacture blinds awnings and shutters. Second generation, in operation for over 30 years.

Final draft must include at minimum:

Business Card (2 Sided)
Letterhead
Presentation Folder

Target Market(s)

home owners, landlords, builders, real estate agents, shopping centres

Industry/Entity Type

Textile

Requirements
Must have
• Design needs to work in mono as well as colour print
Nice to have
• Relevant to the textile industry
Should not have
• The inclusion of blinds, awnings or shutters is an automatic no-no

```html
<!DOCTYPE html>
<html lang="en">
<head>
<meta charset="utf-8">
<title>Harlow Blinds – Business Card</title>
<link href="https://fonts.googleapis.com/css2?family=Arimo:wght@400;700&display=swap" rel="stylesheet">
<style>
  :root {
    --page-bg: #e9e6e1;
    --card-bg: #ffffff;
    --ink-grey: #6d6e71;
    --ink-dark: #58595b;
    --brand-teal: #1aa5a6;
    --mark-grey: #7a7b7e;
    --rule-grey: #8a8b8e;
  }
  * { box-sizing: border-box; margin: 0; padding: 0; }
  html, body {
    width: 1200px;
    height: 794px;
    overflow: hidden;
    background: var(--page-bg);
    font-family: "Arimo", Arial, sans-serif;
  }
  .canvas {
    position: relative;
    width: 1200px;
    height: 794px;
  }
  .card {
    position: absolute;
    top: 247px;
    width: 525px;
    height: 300px;
    background: var(--card-bg);
    box-shadow: 0 2px 10px rgba(0,0,0,0.12);
  }
  .card--front { left: 50px; }
  .card--back { left: 625px; }

  /* Front */
  .front-lockup {
    position: absolute;
    left: 0; right: 0; top: 0; bottom: 0;
    display: flex;
    align-items: center;
    justify-content: center;
    gap: 16px;
  }
  .brand-square {
    width: 70px;
    height: 56px;
    background: var(--mark-grey);
  }
  .brand-rule {
    width: 1px;
    height: 74px;
    background: var(--rule-grey);
  }
  .brand-name {
    color: var(--ink-grey);
    font-size: 30px;
    font-weight: 400;
    line-height: 1;
    letter-spacing: 1px;
    text-transform: uppercase;
  }
  .brand-name span { display: block; }

  /* Back */
  .back-square {
    position: absolute;
    left: 165px;
    top: 130px;
    width: 96px;
    height: 78px;
    background: var(--mark-grey);
  }
  .back-rule {
    position: absolute;
    left: 283px;
    top: 104px;
    width: 1px;
    height: 100px;
    background: var(--rule-grey);
  }
  .contact {
    position: absolute;
    left: 300px;
    top: 66px;
    color: var(--ink-dark);
    font-size: 12.5px;
    line-height: 17px;
  }
  .contact__name {
    color: var(--brand-teal);
    font-weight: 700;
    font-size: 16px;
    line-height: 19px;
    letter-spacing: 0.3px;
  }
  .contact__title {
    color: var(--ink-grey);
    font-size: 12px;
    margin-bottom: 8px;
  }
  .contact__address { margin-bottom: 2px; }
  .contact__line {
    display: flex;
    align-items: center;
    gap: 7px;
  }
  .contact__line svg {
    width: 11px;
    height: 11px;
    flex: none;
    fill: var(--brand-teal);
  }
</style>
</head>
<body>
<main class="canvas">

  <section class="card card--front" aria-label="Business card front">
    <div class="front-lockup">
      <div class="brand-square"></div>
      <div class="brand-rule"></div>
      <div class="brand-name"><span>Harlow</span><span>Blinds</span></div>
    </div>
  </section>

  <section class="card card--back" aria-label="Business card back">
    <div class="back-square"></div>
    <div class="back-rule"></div>
    <div class="contact">
      <p class="contact__name">SAM PORTER</p>
      <p class="contact__title">President</p>
      <p class="contact__address">27 Harbour View Road<br>Airlie Bay, QLD 4802</p>
      <p class="contact__line">
        <svg viewBox="0 0 12 12" aria-hidden="true"><path d="M1 3.5C1 2 2.5 1 6 1s5 1 5 2.5L9.2 5 8 3.8H4L2.8 5zM3 6h6l1.5 5h-9z"/></svg>
        555 0142 7788
      </p>
      <p class="contact__line">
        <svg viewBox="0 0 12 12" aria-hidden="true"><path d="M3 0h6v12H3zM4 1.5v7.5h4V1.5zM5.5 10h1v1h-1z" fill-rule="evenodd"/></svg>
        555 0193 4410
      </p>
      <p class="contact__line">
        <svg viewBox="0 0 12 12" aria-hidden="true"><path d="M0 2.5h12v7H0zM0.8 3l5.2 3.6L11.2 3v0.9L6 7.5 0.8 3.9z" fill-rule="evenodd"/></svg>
        sam@harlowblinds.example
      </p>
      <p class="contact__line">
        <svg viewBox="0 0 12 12" aria-hidden="true"><circle cx="6" cy="6" r="5.5"/><path d="M2 6h8M6 1c-2 2.5-2 7.5 0 10M6 1c2 2.5 2 7.5 0 10" stroke="#fff" stroke-width="0.8" fill="none"/></svg>
        www.harlowblinds.example
      </p>
    </div>
  </section>

</main>
</body>
</html>
```